" Atuamos como laboratório de análises clínicas, oferecendo exames laboratoriais para diagnóstico e prevenção de doenças. Nosso atendimento é feito tanto para pacientes particulares quanto por convênios, com coleta realizada em nossa unidade por profissionais qualificados. Os resultados são disponibilizados de forma rápida, podendo ser acessados online ou retirados presencialmente. Trabalhamos com foco em qualidade, confiabilidade e atendimento humanizado. "

```html
<!DOCTYPE html>
<html lang="pt-BR">
<head>
<meta charset="UTF-8">
<title>Vita Lab — Envelope</title>
<link href="https://fonts.googleapis.com/css2?family=Open+Sans:wght@400;600;700&display=swap" rel="stylesheet">
<style>
  :root {
    --brand-green: #1b8a43;
    --band-soft: rgba(169, 215, 184, 0.35);
    --paper: #ffffff;
    --paper-edge: #e3e3e3;
    --ink: #3a3a3a;
    --ink-soft: #6b6b6b;
    --backdrop: #e8e8e8;
    --window-a: #ecebf0;
    --window-b: #d9d8df;
  }
  * { box-sizing: border-box; margin: 0; padding: 0; }
  html, body { width: 1200px; height: 1200px; overflow: hidden; }
  body {
    background: var(--backdrop);
    font-family: "Open Sans", Arial, sans-serif;
    color: var(--ink);
    position: relative;
  }

  .envelope { position: absolute; left: 216px; width: 768px; height: 456px; }

  /* Front */
  .envelope--front { top: 96px; }
  .envelope__flap-edge {
    position: absolute; top: 0; left: 0; width: 100%; height: 56px;
    background: var(--brand-green); border-radius: 22px 22px 0 0;
  }
  .envelope__body {
    position: absolute; top: 38px; left: 0; width: 100%; height: 418px;
    background: var(--paper); border: 1px solid var(--paper-edge);
  }
  .pulse-band {
    position: absolute; left: 0; top: 104px; width: 100%; height: 60px;
    background: linear-gradient(180deg, transparent 0%, var(--band-soft) 50%, transparent 100%);
  }

  .brand-block {
    position: absolute; left: 60px; top: 20px; width: 252px; height: 96px;
    background: var(--paper); border: 1px solid var(--paper-edge);
    display: flex; align-items: center; gap: 14px; padding-left: 22px;
  }
  .brand-block__dot { width: 34px; height: 34px; border-radius: 50%; background: var(--brand-green); flex: none; }
  .brand-block__text { display: flex; flex-direction: column; }
  .brand-block__name { font-size: 30px; font-weight: 600; color: var(--brand-green); line-height: 1.05; }
  .brand-block__tagline { font-size: 11px; font-weight: 600; color: var(--brand-green); margin-top: 3px; }

  .address-window {
    position: absolute; left: 84px; top: 206px; width: 624px; height: 113px;
    border-radius: 6px; border: 1px solid #cfcfd6;
    background: linear-gradient(135deg, var(--window-a), var(--window-b));
  }

  .contact-bar {
    position: absolute; left: 60px; top: 340px; right: 40px;
    display: flex; align-items: flex-start; gap: 22px; font-size: 10.5px; line-height: 1.45;
  }
  .contact-bar strong { font-weight: 700; }
  .contact-bar__role { color: var(--ink-soft); }
  .contact-bar__item { display: flex; gap: 6px; align-items: flex-start; }
  .contact-bar__icon { width: 13px; height: 13px; flex: none; margin-top: 2px; }

  /* Back */
  .envelope--back { top: 648px; }
  .envelope--back .envelope__sheet {
    position: absolute; inset: 0; background: var(--paper); border: 1px solid var(--paper-edge);
  }
  .envelope__flap { position: absolute; top: 0; left: 0; width: 100%; height: 240px; }
</style>
</head>
<body>

<section class="envelope envelope--front">
  <div class="envelope__flap-edge"></div>
  <div class="envelope__body">
    <div class="pulse-band" role="img" aria-label="Faixa decorativa de linha de batimento cardíaco em verde claro"></div>

    <div class="brand-block">
      <span class="brand-block__dot"></span>
      <div class="brand-block__text">
        <span class="brand-block__name">Vita Lab</span>
        <span class="brand-block__tagline">Laboratório de Análises Clínicas</span>
      </div>
    </div>

    <div class="address-window"></div>

    <div class="contact-bar">
      <div class="contact-bar__people">
        <div><strong>Dr Renato Alves Prado</strong> <span class="contact-bar__role">(Coordenação Médica)</span></div>
        <div><strong>Dra Lúcia Prado</strong> <span class="contact-bar__role">(Coordenação Laboratorial)</span></div>
        <div>contato@vitalab.com.br</div>
      </div>
      <div class="contact-bar__item">
        <svg class="contact-bar__icon" viewBox="0 0 24 24" aria-hidden="true"><path fill="var(--brand-green)" d="M6.6 10.8a15 15 0 0 0 6.6 6.6l2.2-2.2a1 1 0 0 1 1-.25 11.4 11.4 0 0 0 3.6.57 1 1 0 0 1 1 1V20a1 1 0 0 1-1 1A17 17 0 0 1 3 4a1 1 0 0 1 1-1h3.5a1 1 0 0 1 1 1c0 1.25.2 2.45.57 3.57a1 1 0 0 1-.25 1z"/></svg>
        <div>(35) 3200-1100<br>(35) 9 9000-2200</div>
      </div>
      <div class="contact-bar__item">
        <svg class="contact-bar__icon" viewBox="0 0 24 24" aria-hidden="true"><path fill="var(--brand-green)" d="M12 2a7 7 0 0 0-7 7c0 5.2 7 13 7 13s7-7.8 7-13a7 7 0 0 0-7-7zm0 9.5A2.5 2.5 0 1 1 12 6.5a2.5 2.5 0 0 1 0 5z"/></svg>
        <div>Rua das Acácias, 210 - Centro -<br>Serra Alta/MG CEP: 37000-000</div>
      </div>
    </div>
  </div>
</section>

<section class="envelope envelope--back">
  <div class="envelope__sheet"></div>
  <svg class="envelope__flap" viewBox="0 0 768 240" aria-hidden="true">
    <path fill="var(--brand-green)" d="M0,22 Q0,0 22,0 H746 Q768,0 768,22 V52 L452,214 Q384,246 316,214 L0,52 Z"/>
  </svg>
</section>

</body>
</html>
```